Newsletter masthead

We need a masthead for the cover page of our A4 newsletter. It must be 4-5 cms (height) and to fit the whole width of an A4 paper (21cms).

We are a research centre focused on men’s health e.g. male ageing, male obesity and diabetes, prostate cancer research, and male mental health. Our primary readers are researchers, academics, and members of the community.

We’d like to see a masthead that complements our organisation logo (please see attached ATIMH logo). Please note that our Centre logo will be used elsewhere in our newsletter so please do not include the logo in the masthead.

Please include the following words in the masthead:

Lanternmark (name of the newsletter) – please emphasize the ‘men’ part of Lanternmark, if possible.

Men’s health research gathering speed (subtitle of the newsletter)

A Newsletter of the Ashcombe Trust Institute for Men’s Health (origin of the newsletter)

We would like to avoid heavy use of a 3-D effect. We want to keep it simple but modern.

Please note that our Centre logo (attached as ATIMH logo) will be used elsewhere in our newsletter. Please do not include the logo in the masthead. Thank you so much. 

• The masthead could compliment our Centre's logo (please see attached).

Masthead could convey speed or momentum.
• Our Centre's logo.

```html
<!DOCTYPE html>
<html lang="en">
<head>
<meta charset="utf-8">
<title>Lanternmark letterhead sheets</title>
<link rel="stylesheet" href="https://fonts.googleapis.com/css2?family=Carlito:wght@400;700&family=Open+Sans:wght@400;600&display=swap">
<style>
  :root{
    --paper:#ffffff;
    --ink:#1a1a1a;
    --navy:#233f82;
    --navy-light:#4e6fae;
    --navy-deep:#1b3371;
    --green:#3c7f2e;
    --rule:#2c4a78;
    --shadow:rgba(0,0,0,.18);
  }
  *{margin:0;padding:0;box-sizing:border-box}
  html,body{width:1200px;height:1200px;overflow:hidden;background:#fff}
  .canvas{position:relative;width:1200px;height:1200px}
  .sheet{position:absolute;width:540px;background:var(--paper);overflow:hidden;
    box-shadow:0 0 4px var(--shadow);font-family:"Carlito","Calibri",sans-serif;color:var(--ink);--shift:0px}
  .sheet--short{height:380px}
  .sheet--full{height:698px}
  .sheet--wave{--shift:21px}
  .sheet--tl{left:45px;top:65px}
  .sheet--tr{left:615px;top:65px}
  .sheet--bl{left:45px;top:447px}
  .sheet--br{left:615px;top:447px}

  .masthead{position:absolute;left:75px;top:63px;width:390px}
  .masthead svg{display:block}
  .masthead__title{position:absolute;left:11px;top:3px;font-family:"Open Sans",sans-serif;
    font-weight:400;font-size:25px;letter-spacing:-.3px;color:#fff;line-height:1}
  .masthead__tagline{position:absolute;left:12px;top:32px;font-family:"Open Sans",sans-serif;
    font-size:8.6px;color:#fff;line-height:1}
  .masthead__origin{position:absolute;right:7px;top:8px;font-family:"Open Sans",sans-serif;
    font-size:7.4px;color:#fff;line-height:10.5px;text-align:right}

  .meta{position:absolute;left:75px;top:calc(144px + var(--shift));font-size:10px;line-height:25.5px}
  .meta b{font-weight:700}

  .body{position:absolute;left:75px;top:calc(233px + var(--shift));width:395px;font-size:9.7px;line-height:12.65px}
  .body p{margin-bottom:14px;white-space:nowrap}
  .indent{padding-left:9px}

  .signature{position:absolute;left:348px;top:calc(436px + var(--shift));width:130px;height:74px;
    background:linear-gradient(135deg,rgba(0,0,0,0) 40%,rgba(0,0,0,.08) 50%,rgba(0,0,0,0) 60%)}
  .signoff{position:absolute;right:75px;top:calc(489px + var(--shift));font-size:10px;line-height:13px;text-align:right}

  .footer-rule{position:absolute;left:75px;top:645px;width:390px;height:4px;
    background:linear-gradient(var(--rule) 0 70%,var(--green) 70% 100%)}
</style>
</head>
<body>
<div class="canvas">

  <!-- top left: straight masthead -->
  <section class="sheet sheet--short sheet--tl">
    <header class="masthead">
      <svg width="390" height="54" viewBox="0 0 390 54">
        <defs>
          <linearGradient id="bandA" x1="0" y1="0" x2="0" y2="1">
            <stop offset="0" stop-color="#6a86bd"/><stop offset=".45" stop-color="#2c4a8c"/><stop offset="1" stop-color="#1d3675"/>
          </linearGradient>
        </defs>
        <rect width="390" height="51" fill="url(#bandA)"/>
        <path d="M120 51 C200 20 300 18 390 26 V51 Z" fill="#fff" opacity=".08"/>
        <path d="M200 51 C260 36 330 34 390 38 V51 Z" fill="#fff" opacity=".07"/>
        <line x1="0" y1="31" x2="390" y2="31" stroke="#fff" stroke-opacity=".25" stroke-width=".6"/>
        <rect y="50" width="390" height="3" fill="var(--green)"/>
      </svg>
      <div class="masthead__title">LANTERNMARK</div>
      <div class="masthead__tagline">Men’s health research gathering speed</div>
      <div class="masthead__origin">A Newsletter of the Ashcombe Trust<br>Institute for Men’s Health</div>
    </header>
    <div class="meta"><b>From:</b> Project Owner<br><b>To:</b> Personal<br><b>Date:</b> November 27th, 2011</div>
    <div class="body">
      <p><span class="indent">Pellentesque habitant morbi tristique senectus et netus et malesuada fames ac turpis</span><br>egestas. Vestibulum tortor quam, feugiat vitae, ultricies eget, tempor sit amet, ante.<br>Donec eu libero sit amet quam egestas semper. Aenean ultricies mi vitae est. Mauris pla-<br>cerat eleifend leo. Quisque sit amet est et sapien ullamcorper pharetra. Vestibulum erat<br>wisi, condimentum sed, commodo vitae, ornare sit amet, wisi. Aenean fermentum, elit<br>eget tincidunt condimentum, eros ipsum rutrum orci, sagittis tempus lacus enim ac dui.<br>Donec non enim in turpis pulvinar facilisis. Ut felis. Praesent dapibus, neque id cursus fau-<br>cibus, tortor neque egestas augue, eu vulputate magna eros eu erat. Aliquam erat volut-<br>pat. Nam dui mi, tincidunt quis, accumsan porttitor, facilisis luctus, metus</p>
      <p><span class="indent">Pellentesque habitant morbi tristique senectus et netus et malesuada fames ac turpis</span><br>egestas. Vestibulum tortor quam, feugiat vitae, ultricies eget, tempor sit amet, ante.</p>
    </div>
  </section>

  <!-- top right: wave masthead -->
  <section class="sheet sheet--short sheet--tr sheet--wave">
    <header class="masthead">
      <svg width="390" height="84" viewBox="0 0 390 84">
        <defs>
          <linearGradient id="bandB" x1="0" y1="0" x2="0" y2="1">
            <stop offset="0" stop-color="#6a86bd"/><stop offset=".35" stop-color="#2c4a8c"/><stop offset="1" stop-color="#1d3675"/>
          </linearGradient>
        </defs>
        <path d="M0 0 H390 V52 C330 84 270 82 200 68 C130 54 60 58 0 76 Z" fill="url(#bandB)"/>
        <path d="M150 70 C230 40 320 30 390 36 V52 C330 84 270 82 200 68 Z" fill="#fff" opacity=".08"/>
        <line x1="0" y1="33" x2="390" y2="33" stroke="#fff" stroke-opacity=".25" stroke-width=".6"/>
        <path d="M0 76 C60 58 130 54 200 68 C270 82 330 84 390 52" fill="none" stroke="var(--green)" stroke-width="2.5"/>
      </svg>
      <div class="masthead__title">LANTERNMARK</div>
      <div class="masthead__tagline" style="top:35px">Men’s health research gathering speed</div>
      <div class="masthead__origin">A Newsletter of the Ashcombe Trust<br>Institute for Men’s Health</div>
    </header>
    <div class="meta"><b>From:</b> Project Owner<br><b>To:</b> Personal<br><b>Date:</b> November 27th, 2011</div>
    <div class="body">
      <p><span class="indent">Pellentesque habitant morbi tristique senectus et netus et malesuada fames ac turpis</span><br>egestas. Vestibulum tortor quam, feugiat vitae, ultricies eget, tempor sit amet, ante.<br>Donec eu libero sit amet quam egestas semper. Aenean ultricies mi vitae est. Mauris pla-<br>cerat eleifend leo. Quisque sit amet est et sapien ullamcorper pharetra. Vestibulum erat<br>wisi, condimentum sed, commodo vitae, ornare sit amet, wisi. Aenean fermentum, elit<br>eget tincidunt condimentum, eros ipsum rutrum orci, sagittis tempus lacus enim ac dui.<br>Donec non enim in turpis pulvinar facilisis. Ut felis. Praesent dapibus, neque id cursus fau-<br>cibus, tortor neque egestas augue, eu vulputate magna eros eu erat. Aliquam erat volut-<br>pat. Nam dui mi, tincidunt quis, accumsan porttitor, facilisis luctus, metus</p>
    </div>
  </section>

  <!-- bottom left: straight masthead, full letter -->
  <section class="sheet sheet--full sheet--bl">
    <header class="masthead">
      <svg width="390" height="54" viewBox="0 0 390 54">
        <rect width="390" height="51" fill="url(#bandA)"/>
        <path d="M120 51 C200 20 300 18 390 26 V51 Z" fill="#fff" opacity=".08"/>
        <path d="M200 51 C260 36 330 34 390 38 V51 Z" fill="#fff" opacity=".07"/>
        <line x1="0" y1="31" x2="390" y2="31" stroke="#fff" stroke-opacity=".25" stroke-width=".6"/>
        <rect y="50" width="390" height="3" fill="var(--green)"/>
      </svg>
      <div class="masthead__title">LANTERNMARK</div>
      <div class="masthead__tagline">Men’s health research gathering speed</div>
      <div class="masthead__origin">A Newsletter of the Ashcombe Trust<br>Institute for Men’s Health</div>
    </header>
    <div class="meta"><b>From:</b> Project Owner<br><b>To:</b> Personal<br><b>Date:</b> November 27th, 2011</div>
    <div class="body">
      <p><span class="indent">Pellentesque habitant morbi tristique senectus et netus et malesuada fames ac turpis</span><br>egestas. Vestibulum tortor quam, feugiat vitae, ultricies eget, tempor sit amet, ante.<br>Donec eu libero sit amet quam egestas semper. Aenean ultricies mi vitae est. Mauris pla-<br>cerat eleifend leo. Quisque sit amet est et sapien ullamcorper pharetra. Vestibulum erat<br>wisi, condimentum sed, commodo vitae, ornare sit amet, wisi. Aenean fermentum, elit<br>eget tincidunt condimentum, eros ipsum rutrum orci, sagittis tempus lacus enim ac dui.<br>Donec non enim in turpis pulvinar facilisis. Ut felis. Praesent dapibus, neque id cursus fau-<br>cibus, tortor neque egestas augue, eu vulputate magna eros eu erat. Aliquam erat volut-<br>pat. Nam dui mi, tincidunt quis, accumsan porttitor, facilisis luctus, metus</p>
      <p><span class="indent">Pellentesque habitant morbi tristique senectus et netus et malesuada fames ac turpis</span><br>egestas. Vestibulum tortor quam, feugiat vitae, ultricies eget, tempor sit amet, ante.<br>Donec eu libero sit amet quam egestas semper. Aenean ultricies mi vitae est. Mauris pla-<br>cerat eleifend leo.</p>
    </div>
    <div class="signature" role="img" aria-label="Handwritten signature of the sender"></div>
    <div class="signoff">Project Owner<br>General Manager</div>
    <div class="footer-rule"></div>
  </section>

  <!-- bottom right: wave masthead, full letter -->
  <section class="sheet sheet--full sheet--br sheet--wave">
    <header class="masthead">
      <svg width="390" height="84" viewBox="0 0 390 84">
        <path d="M0 0 H390 V52 C330 84 270 82 200 68 C130 54 60 58 0 76 Z" fill="url(#bandB)"/>
        <path d="M150 70 C230 40 320 30 390 36 V52 C330 84 270 82 200 68 Z" fill="#fff" opacity=".08"/>
        <line x1="0" y1="33" x2="390" y2="33" stroke="#fff" stroke-opacity=".25" stroke-width=".6"/>
        <path d="M0 76 C60 58 130 54 200 68 C270 82 330 84 390 52" fill="none" stroke="var(--green)" stroke-width="2.5"/>
      </svg>
      <div class="masthead__title">LANTERNMARK</div>
      <div class="masthead__tagline" style="top:35px">Men’s health research gathering speed</div>
      <div class="masthead__origin">A Newsletter of the Ashcombe Trust<br>Institute for Men’s Health</div>
    </header>
    <div class="meta"><b>From:</b> Project Owner<br><b>To:</b> Personal<br><b>Date:</b> November 27th, 2011</div>
    <div class="body">
      <p><span class="indent">Pellentesque habitant morbi tristique senectus et netus et malesuada fames ac turpis</span><br>egestas. Vestibulum tortor quam, feugiat vitae, ultricies eget, tempor sit amet, ante.<br>Donec eu libero sit amet quam egestas semper. Aenean ultricies mi vitae est. Mauris pla-<br>cerat eleifend leo. Quisque sit amet est et sapien ullamcorper pharetra. Vestibulum erat<br>wisi, condimentum sed, commodo vitae, ornare sit amet, wisi. Aenean fermentum, elit<br>eget tincidunt condimentum, eros ipsum rutrum orci, sagittis tempus lacus enim ac dui.<br>Donec non enim in turpis pulvinar facilisis. Ut felis. Praesent dapibus, neque id cursus fau-<br>cibus, tortor neque egestas augue, eu vulputate magna eros eu erat. Aliquam erat volut-<br>pat. Nam dui mi, tincidunt quis, accumsan porttitor, facilisis luctus, metus</p>
      <p><span class="indent">Pellentesque habitant morbi tristique senectus et netus et malesuada fames ac turpis</span><br>egestas. Vestibulum tortor quam, feugiat vitae, ultricies eget, tempor sit amet, ante.<br>Donec eu libero sit amet quam egestas semper. Aenean ultricies mi vitae est. Mauris pla-<br>cerat eleifend leo.</p>
    </div>
    <div class="signature" role="img" aria-label="Handwritten signature of the sender"></div>
    <div class="signoff">Project Owner<br>General Manager</div>
    <div class="footer-rule"></div>
  </section>

</div>
</body>
</html>
```